LOGO and Business Card Design Project

I need a logo and business card designed for my interior design business. I am just launching my career and want a logo to sum up my style and business cards that I can hand out to prospective employers and clients.
The logo is the most important aspect. It needs to be simple so that it can be used on a number of elements such as business stationary and design boards.
Zentrix top logos of 2012 to see how a simple logo can be really effective at conveying a business identity.
My logo and business card need to quickly express my style.
In a nutshell my style is classic with an edge. If I were in the fashion world my look would be aspiring to be Benedict Oakhurst - velvet storm is a big inspiration.
The name is Tova Interiors. Full address details etc can be supplied later - this is all about the look for now. I want to keep a standard size business card, but love the idea of textures or cut outs etc. This card and logo need to help me stand out from the crowd.

```html
<!DOCTYPE html>
<html lang="en">
<head>
<meta charset="utf-8">
<title>Tova Interiors – Business Card</title>
<link rel="stylesheet" href="https://fonts.googleapis.com/css2?family=Cutive+Mono&display=swap">
<style>
  :root {
    --backdrop: #d6d6d6;
    --damask-navy: #3b4468;
    --damask-sand: #b7ad93;
    --damask-mist: #8d8f98;
    --panel-white: #f3f2f6;
    --frame-silver: #9a9a9e;
    --frame-shadow: #5c5c62;
    --ink-dark: #2a2a2e;
    --ink-light: #f7f7f9;
  }
  * { margin: 0; padding: 0; box-sizing: border-box; }
  html, body {
    width: 1200px; height: 900px; overflow: hidden;
    background: var(--backdrop);
  }
  .stage {
    position: relative; width: 1200px; height: 900px;
  }
  .card {
    position: absolute; left: 285px; width: 630px; height: 360px;
    box-shadow: 0 6px 18px rgba(0,0,0,0.25);
    overflow: hidden;
  }
  .card--front { top: 70px; }
  .card--back { top: 480px; }
  .damask-texture {
    position: absolute; inset: 0;
    background:
      radial-gradient(ellipse at 40% 35%, rgba(183,173,147,0.55), transparent 65%),
      linear-gradient(135deg, var(--damask-sand) 0%, var(--damask-mist) 45%, var(--damask-navy) 100%);
  }
  .frame {
    position: absolute;
    background: var(--panel-white);
    border: 6px double var(--frame-silver);
    outline: 2px solid var(--frame-shadow);
    outline-offset: 2px;
    box-shadow: 0 4px 10px rgba(0,0,0,0.35);
    display: flex; flex-direction: column; align-items: center; justify-content: center;
    font-family: "Cutive Mono", monospace;
    text-align: center;
  }
  .frame--logo {
    left: 205px; top: 40px; width: 220px; height: 180px;
  }
  .brand-name {
    font-size: 30px; line-height: 1.1; color: var(--ink-dark);
  }
  .frame--contact {
    left: 95px; top: 70px; width: 440px; height: 220px;
    color: var(--ink-dark);
  }
  .contact-name { font-size: 30px; margin-bottom: 8px; }
  .contact-line { font-size: 19px; line-height: 1.25; }
</style>
</head>
<body>
<main class="stage">
  <section class="card card--front">
    <div class="damask-texture" role="img" aria-label="Blue damask wallpaper pattern on a worn sand-coloured ground"></div>
    <div class="frame frame--logo">
      <p class="brand-name">Tova<br>Interiors</p>
    </div>
  </section>

  <section class="card card--back">
    <div class="damask-texture" role="img" aria-label="Blue damask wallpaper pattern on a worn sand-coloured ground"></div>
    <div class="frame frame--contact">
      <p class="contact-name">Mara Quill</p>
      <p class="contact-line">5678 Elm Row</p>
      <p class="contact-line">London</p>
      <p class="contact-line">+44 5550 19283</p>
      <p class="contact-line">mara@tova.com | www.tova.com</p>
    </div>
  </section>
</main>
</body>
</html>
```